Spectacular Business Card Design for AI SAAS Plattform called Leapvine.ai

Hi Creators
I need an outstanding new Design for my business card.
I run an AI automated Saas Plattform Called Leapvine.ai

Front side:
Logo
Slogan: DIY Business Development & Social Media Management
Data:
Name: Markus Obelwinter - CEO / Founder
email: m.obelwinter@leapvine.ai
mobile: +43 699 82 37 415

Company name:
Leapvine FlexCo

Backside:

What we stand for Slogan:
Vertrauen in KI-Technologie, getragen von menschlicher Vision: Dein Sprung nach vorn!
+ a fancy design what captures our core competencies - AI automisations, Social Media Management, Business development
(dont know if its too much, but AI and social media should be )

pls find attached the logo and the old design

Industry/Entity Type

AI automations for marketing and business development

Contact Information for Business Card

Front side: Logo Slogan: DIY Business Development & Social Media Management Data: Name: Markus Obelwinter - CEO / Founder email: m.obelwinter@leapvine.ai mobile: +43 699 82 37 415 Company name: Leapvine FlexCo Backside: What we stand for Slogan: Vertrauen in KI-Technologie, getragen von menschlicher Vision: Dein Sprung nach vorn!

Font styles to use
Serif
Sans Serif

Requirements
Nice to have
• a fancy design on the backside, a fancy design what captures our core competencies - AI automisations, Social Media Management, Business development

```html
<!DOCTYPE html>
<html lang="en">
<head>
<meta charset="utf-8">
<title>Leapvine.ai – Business Card</title>
<link rel="stylesheet" href="https://fonts.googleapis.com/css2?family=Montserrat:wght@400;500;700&display=swap">
<style>
  :root {
    --bg: #d2d2d2;
    --paper: #efefed;
    --teal: #0b8ca4;
    --teal-deep: #0a7f96;
    --orange: #f28c2c;
    --grey: #6f6f6f;
    --white: #ffffff;
  }
  * { box-sizing: border-box; margin: 0; padding: 0; }
  html, body {
    width: 1200px; height: 1051px; overflow: hidden;
    background: var(--bg);
    font-family: "Montserrat", Arial, sans-serif;
  }
  .sheet {
    width: 1200px; height: 1051px;
    display: flex; flex-direction: column; align-items: center; justify-content: center;
    gap: 56px;
  }
  .card {
    width: 760px; height: 440px; position: relative;
    box-shadow: 0 14px 30px rgba(0,0,0,0.18);
  }
  /* Front */
  .card--front { background: var(--paper); }
  .brand {
    position: absolute; left: 60px; top: 130px; width: 300px;
    display: flex; align-items: center; gap: 14px;
  }
  .brand__mark { width: 26px; height: 26px; background: var(--orange); flex: none; }
  .brand__name { font-size: 50px; font-weight: 500; color: var(--teal); letter-spacing: 0.5px; }
  .divider {
    position: absolute; left: 398px; top: 70px; width: 2px; height: 230px;
    background: #d6d6d4;
  }
  .contact { position: absolute; left: 432px; top: 90px; }
  .contact__name { font-size: 27px; font-weight: 700; color: var(--teal); }
  .contact__role { font-size: 17px; color: var(--grey); margin-top: 6px; }
  .contact__company { font-size: 17px; color: var(--teal); margin-top: 16px; }
  .contact__list { list-style: none; margin-top: 22px; }
  .contact__item {
    display: flex; align-items: center; gap: 10px;
    font-size: 17px; color: var(--grey); margin-bottom: 6px;
  }
  .contact__icon { width: 14px; height: 14px; flex: none; }
  .tagline {
    position: absolute; left: 60px; bottom: 48px;
    font-size: 17px; color: var(--grey); letter-spacing: 0.3px;
  }
  /* Back */
  .card--back { background: var(--teal); border-bottom: 8px solid var(--teal-deep); }
  .brand--back {
    position: absolute; left: 0; right: 0; top: 120px;
    display: flex; justify-content: center; align-items: center; gap: 14px;
  }
  .brand--back .brand__name { color: var(--white); font-size: 54px; }
  .statement {
    position: absolute; left: 0; right: 0; top: 236px;
    text-align: center; color: var(--white); font-size: 16px; line-height: 1.55;
  }
  .statement__accent { color: var(--orange); }
</style>
</head>
<body>
<main class="sheet">
  <section class="card card--front" aria-label="Business card front">
    <div class="brand">
      <span class="brand__mark"></span>
      <span class="brand__name">Leapvine</span>
    </div>
    <div class="divider"></div>
    <div class="contact">
      <p class="contact__name">Markus Obelwinter</p>
      <p class="contact__role">CEO / Founder</p>
      <p class="contact__company">Leapvine FlexCo</p>
      <ul class="contact__list">
        <li class="contact__item">
          <svg class="contact__icon" viewBox="0 0 24 24" aria-hidden="true"><path fill="#f28c2c" d="M6.6 10.8a15.1 15.1 0 0 0 6.6 6.6l2.2-2.2c.3-.3.7-.4 1-.2 1.1.4 2.3.6 3.6.6.6 0 1 .4 1 1V20c0 .6-.4 1-1 1A17 17 0 0 1 3 4c0-.6.4-1 1-1h3.5c.6 0 1 .4 1 1 0 1.3.2 2.5.6 3.6.1.3 0 .7-.2 1z"/></svg>
          +43 699 82 37 415
        </li>
        <li class="contact__item">
          <svg class="contact__icon" viewBox="0 0 24 24" aria-hidden="true"><path fill="#f28c2c" d="M2 5h20v14H2z"/><path fill="none" stroke="#efefed" stroke-width="2" d="M2 6l10 7 10-7"/></svg>
          m.obelwinter@leapvine.ai
        </li>
        <li class="contact__item">
          <svg class="contact__icon" viewBox="0 0 24 24" aria-hidden="true"><circle cx="12" cy="12" r="10" fill="#f28c2c"/><path fill="none" stroke="#efefed" stroke-width="1.5" d="M2 12h20M12 2c3 3 3 17 0 20M12 2c-3 3-3 17 0 20"/></svg>
          www.leapvine.ai
        </li>
      </ul>
    </div>
    <p class="tagline">DIY Business Development &amp; Social Media Management</p>
  </section>

  <section class="card card--back" aria-label="Business card back">
    <div class="brand brand--back">
      <span class="brand__mark"></span>
      <span class="brand__name">Leapvine</span>
    </div>
    <div class="statement">
      <p class="statement__accent">What we stand for Slogan:</p>
      <p>Vertrauen in KI-Technologie, getragen von menschlicher</p>
      <p><span class="statement__accent">Vision:</span> Dein Sprung nach vorn!</p>
      <p>+ a fancy design what captures our core competencies -</p>
      <p>AI automisations, Social Media Management, Business development</p>
    </div>
  </section>
</main>
</body>
</html>
```